Employee Handbook Cover

We need an cover for our employee handbook. The handbook should convey our core values of
-Family
-Accountability
-Professionalism
Attached is our logo. Please visit our website to get a feeling for what we do at www.brivolamfg.com

```html
<!DOCTYPE html>
<html lang="en">
<head>
<meta charset="utf-8">
<title>Brivola Employee Handbook Cover</title>
<link href="https://fonts.googleapis.com/css2?family=Roboto:wght@400;700;900&display=swap" rel="stylesheet">
<style>
  :root {
    --brand-blue: #283593;
    --paper: #ffffff;
    --backdrop: #e9e9ea;
  }
  html, body {
    margin: 0;
    width: 800px;
    height: 1200px;
    overflow: hidden;
    background: var(--backdrop);
    font-family: "Roboto", Arial, sans-serif;
  }
  .spread {
    position: absolute;
    left: 20px;
    top: 466px;
    width: 760px;
    height: 268px;
    display: block;
    box-shadow: 0 6px 18px rgba(0,0,0,0.18);
  }
  .brand-name {
    font-family: "Roboto", Arial, sans-serif;
    font-weight: 900;
    fill: var(--brand-blue);
  }
  .imprint {
    font-family: "Roboto", Arial, sans-serif;
    fill: var(--paper);
  }
  .cover-title {
    font-family: "Roboto", Arial, sans-serif;
    font-weight: 400;
    fill: var(--paper);
    letter-spacing: 0.3px;
  }
</style>
</head>
<body>
<svg class="spread" viewBox="0 0 850 300" xmlns="http://www.w3.org/2000/svg">
  <defs>
    <linearGradient id="gearFill" x1="0" y1="0" x2="1" y2="1">
      <stop offset="0" stop-color="#3a55c8"/>
      <stop offset="1" stop-color="#1a2370"/>
    </linearGradient>
    <linearGradient id="officeFill" x1="0" y1="0" x2="0" y2="1">
      <stop offset="0" stop-color="#b9b4ad"/>
      <stop offset="1" stop-color="#7a5a40"/>
    </linearGradient>
    <linearGradient id="weldFill" x1="0" y1="0" x2="1" y2="1">
      <stop offset="0" stop-color="#5c5f66"/>
      <stop offset="0.55" stop-color="#c9d4e6"/>
      <stop offset="1" stop-color="#6e6a66"/>
    </linearGradient>
    <linearGradient id="cargoFill" x1="0" y1="0" x2="0" y2="1">
      <stop offset="0" stop-color="#3c4f86"/>
      <stop offset="1" stop-color="#b48c6c"/>
    </linearGradient>
  </defs>

  <!-- Cover base -->
  <rect class="paper" x="0" y="0" width="850" height="300" fill="var(--paper)"/>
  <rect class="band" x="0" y="130" width="850" height="170" fill="var(--brand-blue)"/>

  <!-- Back cover -->
  <g class="back-cover">
    <polygon role="img" aria-label="Close-up photo of blue machine gears"
             points="292,93 403,93 320,275 235,275" fill="url(#gearFill)"/>

    <circle cx="157" cy="105" r="11" fill="var(--brand-blue)"/>
    <text class="brand-name" x="172" y="113" font-size="22">Brivola</text>

    <text class="imprint" x="224" y="240" font-size="7.5" text-anchor="end">Brivola International Corp.</text>
    <text class="imprint" x="224" y="249" font-size="5" text-anchor="end">4120, Harlow Ave. Corvane, TX70154</text>
    <text class="imprint" x="224" y="257" font-size="5" text-anchor="end">Tel 555 014 2290</text>
  </g>

  <!-- Front cover -->
  <g class="front-cover">
    <polygon role="img" aria-label="Photo of staff working in an office"
             points="547,128 615,128 555,285 487,285" fill="url(#officeFill)"/>
    <polygon role="img" aria-label="Photo of a welder at work with sparks"
             points="645,12 765,12 697,210 610,210" fill="url(#weldFill)"/>
    <polygon role="img" aria-label="Photo of a warehouse worker moving boxes on a hand truck"
             points="775,65 838,65 760,285 680,285" fill="url(#cargoFill)"/>

    <circle cx="478" cy="59" r="12" fill="var(--brand-blue)"/>
    <text class="brand-name" x="496" y="68" font-size="25">Brivola</text>

    <text class="cover-title" x="650" y="277" font-size="9.5">EMPLOYEE HANDBOOK</text>
  </g>
</svg>
</body>
</html>
```